Business Card Design for a Personal Trainer

I need a business card design for my job as a personal trainer. It should have a unique, modern and exclusive design. On the front there should be only my logo with my name and my job. 0163/2918374 Tobias Kellinger Lindenfeldweg 14 80412 Munich Germany The most important contact information is the web adress. it can be bigger than the rest, but its not necessary. The card should be 8,5cmx5,5cm big. Font: Roboto. Colors: black, white, gray, 56c1ff.

```html
<!DOCTYPE html>
<html lang="de">
<head>
<meta charset="utf-8">
<title>Tobias Kellinger – Business Cards</title>
<link rel="stylesheet" href="https://fonts.googleapis.com/css2?family=Roboto:wght@400&family=Roboto+Condensed:wght@400;500&display=swap">
<style>
  :root {
    --canvas: #eef0f0;
    --card-dark: #4b4b4b;
    --card-light: #ffffff;
    --accent: #56c1ff;
    --ink-light: #ffffff;
    --ink-dark: #2b2b2b;
    --photo-dark-a: #626262;
    --photo-dark-b: #2e2e2e;
    --photo-light-a: #8a8a8a;
    --photo-light-b: #353535;
  }
  * { box-sizing: border-box; margin: 0; padding: 0; }
  html, body { width: 1200px; height: 1200px; overflow: hidden; }
  body { background: var(--canvas); position: relative; }

  .card {
    position: absolute;
    width: 314px;
    height: 487px;
    border-radius: 17px;
    overflow: hidden;
    box-shadow: 0 4px 10px rgba(0,0,0,0.12);
  }
  .card--dark { background: var(--card-dark); }
  .card--light { background: var(--card-light); }

  .pos-front-dark { left: 272px; top: 99px; }
  .pos-back-dark { left: 615px; top: 99px; }
  .pos-front-light { left: 272px; top: 613px; }
  .pos-back-light { left: 615px; top: 613px; }

  /* front */
  .brand {
    position: absolute;
    left: 0; right: 0; top: 268px;
    text-align: center;
    font-family: "Roboto", sans-serif;
    color: var(--accent);
  }
  .brand__name {
    display: inline-flex;
    align-items: center;
    gap: 10px;
    font-size: 22px;
    font-weight: 400;
    letter-spacing: 0.5px;
    text-transform: uppercase;
  }
  .brand__mark {
    width: 14px; height: 14px;
    background: var(--accent);
  }
  .brand__role {
    margin-top: 4px;
    font-size: 10px;
    letter-spacing: 2.5px;
    text-transform: uppercase;
  }

  /* back: portrait silhouette kept clear of the contact column */
  .portrait {
    position: absolute;
    left: 0; top: 34px;
    width: 218px; height: 453px;
    clip-path: polygon(30px 0, 118px 0, 122px 118px, 218px 156px, 218px 100%, 0 100%, 0 146px, 26px 118px);
  }
  .card--dark .portrait {
    background: linear-gradient(180deg, var(--photo-dark-a) 0%, var(--photo-dark-b) 100%);
  }
  .card--light .portrait {
    background: linear-gradient(180deg, var(--photo-light-a) 0%, var(--photo-light-b) 100%);
  }

  .contact {
    position: absolute;
    right: 34px; top: 54px;
    text-align: right;
    font-family: "Roboto Condensed", sans-serif;
    text-transform: uppercase;
    letter-spacing: 0.6px;
  }
  .contact__name {
    font-size: 15px;
    font-weight: 500;
    color: var(--accent);
    letter-spacing: 1px;
  }
  .contact__block { margin-top: 12px; font-size: 11px; line-height: 16px; }
  .card--dark .contact__block { color: var(--ink-light); }
  .card--light .contact__block { color: var(--ink-dark); }

  .web-band {
    position: absolute;
    left: 36px; bottom: 0;
    width: 242px; height: 52px;
    background: var(--accent);
    color: var(--ink-light);
    font-family: "Roboto Condensed", sans-serif;
    font-weight: 500;
    font-size: 17px;
    letter-spacing: 0.3px;
    text-transform: uppercase;
    display: flex; align-items: center; justify-content: center;
  }
</style>
</head>
<body>

  <section class="card card--dark pos-front-dark">
    <div class="brand">
      <div class="brand__name"><span class="brand__mark"></span>Tobias Kellinger</div>
      <div class="brand__role">Personal Trainer</div>
    </div>
  </section>

  <section class="card card--dark pos-back-dark">
    <div class="portrait" role="img" aria-label="Black and white portrait of the trainer with arms crossed"></div>
    <div class="contact">
      <div class="contact__name">Tobias Kellinger</div>
      <div class="contact__block">Lindenfeldweg 14<br>80412 München</div>
      <div class="contact__block">0163/2918374<br>t.kellinger@postfach.de</div>
    </div>
    <div class="web-band">www.tobiaskellinger.de</div>
  </section>

  <section class="card card--light pos-front-light">
    <div class="brand">
      <div class="brand__name"><span class="brand__mark"></span>Tobias Kellinger</div>
      <div class="brand__role">Personal Trainer</div>
    </div>
  </section>

  <section class="card card--light pos-back-light">
    <div class="portrait" role="img" aria-label="Black and white portrait of the trainer with arms crossed"></div>
    <div class="contact">
      <div class="contact__name">Tobias Kellinger</div>
      <div class="contact__block">Lindenfeldweg 14<br>80412 München</div>
      <div class="contact__block">0163/2918374<br>t.kellinger@postfach.de</div>
    </div>
    <div class="web-band">www.tobiaskellinger.de</div>
  </section>

</body>
</html>
```